Design a Small Graphic for a client brochure and Website

We need a a fairly simple diagram/graphic to replace the existing graphic in our brochures and website. We are a Private Wealth Advice firm, dealing with high-end clients. We would like to be able to copyright the final design. We need this design to be stylish and have a long shelf-life.
The original design is quite old and was not updated to reflect our company growth or changes in our website design and brochure designs.
Updates

Target Market(s)

Private Wealth clients
High end
Age 45 plus

Industry/Entity Type

Finance

Font styles to use
Sans Serif
Other font styles liked:
• Stag Sans

Requirements
Must have
• Corporate colours only - plus white
• Pantone 288c (Blue)
• Pantone Cool grey 10c
• Pantone 666c (purple - only limited use for highlighting etc)
• Corporate fonts only
• Stag Sans light, book and thin
• Must provide AI editable files
• Must be able to scale to size and remove/replace any text
• Must be in keeping with our brochures and website which can be viewed at www.ridgefold-advisory.com.au
Nice to have
• We want something more vibrant than the image we are using. Something which is in keeping with our image but that is really eye catching.

```html
<!DOCTYPE html>
<html lang="en">
<head>
<meta charset="utf-8">
<title>Client Service Wheel</title>
<link rel="stylesheet" href="https://fonts.googleapis.com/css2?family=Open+Sans:wght@400;500&display=swap">
<style>
  :root {
    --brand-blue: #012f70;
    --cool-grey: #63666a;
    --accent-purple: #a497bf;
    --white: #ffffff;
  }
  html, body {
    margin: 0;
    padding: 0;
    width: 1200px;
    height: 1000px;
    overflow: hidden;
    background: var(--white);
  }
  .canvas {
    width: 1200px;
    height: 1000px;
    display: block;
  }
  .wheel-segment { fill: var(--brand-blue); }
  .wheel-gap { fill: var(--white); }
  .wheel-hub { fill: var(--white); }
  .connector-arc {
    fill: none;
    stroke: var(--accent-purple);
    stroke-width: 3;
  }
  .segment-label {
    font-family: "Open Sans", sans-serif;
    font-size: 12.5px;
    font-weight: 400;
    letter-spacing: 1.6px;
    fill: var(--white);
  }
  .hub-label {
    font-family: "Open Sans", sans-serif;
    font-size: 21px;
    font-weight: 400;
    fill: var(--cool-grey);
  }
</style>
</head>
<body>
<svg class="canvas" viewBox="0 0 1200 1000" xmlns="http://www.w3.org/2000/svg" role="img" aria-label="Client service wheel: Your Legacy, Your Purpose, Wealth Planning and Investment Consulting around the client">
  <defs>
    <path id="path-legacy-outer" d="M495.8 603.2 A146 146 0 0 1 702.2 396.8"/>
    <path id="path-legacy-inner" d="M513.4 585.6 A121 121 0 0 1 684.6 414.4"/>
    <path id="path-purpose-outer" d="M495.8 396.8 A146 146 0 0 1 702.2 603.2"/>
    <path id="path-purpose-inner" d="M513.4 414.4 A121 121 0 0 1 684.6 585.6"/>
    <path id="path-investment-inner" d="M509.9 410.9 A126 126 0 0 0 688.1 589.1"/>
    <path id="path-investment-outer" d="M490.1 391.1 A154 154 0 0 0 707.9 608.9"/>
    <path id="path-wealth-inner" d="M509.9 589.1 A126 126 0 0 0 688.1 410.9"/>
    <path id="path-wealth-outer" d="M490.1 608.9 A154 154 0 0 0 707.9 391.1"/>
  </defs>

  <g class="wheel">
    <circle class="wheel-segment" cx="599.5" cy="500" r="216.5"/>
    <rect class="wheel-gap" x="592" y="270" width="15" height="460"/>
    <rect class="wheel-gap" x="370" y="492.5" width="460" height="15.5"/>
    <circle class="wheel-hub" cx="599.5" cy="500" r="77"/>
  </g>

  <g class="connectors">
    <path class="connector-arc" d="M561.3 348.6 A156 156 0 0 1 636.7 348.6"/>
    <path class="connector-arc" d="M750.4 462.3 A156 156 0 0 1 750.4 537.7"/>
    <path class="connector-arc" d="M636.7 651.4 A156 156 0 0 1 561.3 651.4"/>
    <path class="connector-arc" d="M447.6 537.7 A156 156 0 0 1 447.6 462.3"/>
  </g>

  <g class="labels">
    <text class="segment-label"><textPath href="#path-legacy-outer" startOffset="50%" text-anchor="middle">YOUR</textPath></text>
    <text class="segment-label"><textPath href="#path-legacy-inner" startOffset="50%" text-anchor="middle">LEGACY</textPath></text>

    <text class="segment-label"><textPath href="#path-purpose-outer" startOffset="50%" text-anchor="middle">YOUR</textPath></text>
    <text class="segment-label"><textPath href="#path-purpose-inner" startOffset="50%" text-anchor="middle">PURPOSE</textPath></text>

    <text class="segment-label"><textPath href="#path-investment-inner" startOffset="50%" text-anchor="middle">INVESTMENT</textPath></text>
    <text class="segment-label"><textPath href="#path-investment-outer" startOffset="50%" text-anchor="middle">CONSULTING</textPath></text>

    <text class="segment-label"><textPath href="#path-wealth-inner" startOffset="50%" text-anchor="middle">WEALTH</textPath></text>
    <text class="segment-label"><textPath href="#path-wealth-outer" startOffset="50%" text-anchor="middle">PLANNING</textPath></text>

    <text class="hub-label" x="599.5" y="508" text-anchor="middle">Client</text>
  </g>
</svg>
</body>
</html>
```